Touch screen based web site design

We have a product called vLoop.

It is a browser based touch screen application for the apartment leasing industry . You can read more about it at http://vloop.corvelbrook.example.

To see how the product functions, you can check the link http://www.webvloopdesk.example/vloop.aspx?k=demo1.

We have a need to give a new look and feel to the application. The redesign is NOT to be limited to colors and shapes, but an overhaul of the screen layout, color, font scheme to make the application flow nice and smooth. The content of the pages will remain the same.

There will be animations but that can be done by our IT team, if described in concept by the designer.

Again to reiterate, all things are up for grab, do not get influenced by the images, shapes and color used currently.
Updates

Project Deadline Extended
Reason: None of the design are coming even close to what I am asking for. Please see the homepage of the application at http://www.corvelbrook.example/vloop/images/img-screenshot-lg-01.jpg. That is what I am asking for as the first page to show the design idea.

Project Deadline Extended
Reason: At least the last couple of designs submitted understands it is a touch screen and the home page is not a web site home page. The reason I am still not able to select a design is that the quality of graphic design elements is sub par. For example, The treatment to the options for example are not sharp and up to mark.

Target Market(s)

Propective residents walking into a apartment leasing centers

Industry/Entity Type

Apartment

Requirements
Must have
• - Must have a design where the content, like name of the property, menu options and pictures, are dynamic. So for example, do not restrict the design in a manner that we cannot switch off an option without redesign of the page.
- Good use of icons for options
- Gives the user a calm and serene feeling while maintaining a crisp modern user interface
Nice to have
• - Design in a manner that the background can be a custom image for a specific client
- Description of animation on the screen where the images selected by the client can rotate/slide/appear/animate
Should not have
• - Boxy design
- Small options that cannot be touched by fingers
- dont plan on hover animations, will not work in touch

```html
<!DOCTYPE html>
<html lang="en">
<head>
<meta charset="utf-8">
<title>vLoop – Fitness Center</title>
<link href="https://fonts.googleapis.com/css2?family=Arimo:wght@400;700&family=Roboto+Condensed:wght@700&display=swap" rel="stylesheet">
<style>
:root{
  --bar-top:#5e6469;
  --bar-bottom:#3a3e43;
  --rule:#0c0d0e;
  --ink:#38393c;
  --ink-soft:#3f4044;
  --menu-light:#ffffff;
  --menu-dark:#cfcfcf;
  --accent-light:#f39c25;
  --accent-dark:#e8621a;
  --stage-light:#f5f5f5;
  --stage-dark:#e2e2e2;
  --white:#ffffff;
}
*{box-sizing:border-box;margin:0;padding:0}
html,body{width:1200px;height:648px;overflow:hidden}
body{position:relative;font-family:"Arimo",Arial,sans-serif;background:var(--stage-dark)}
.masthead{
  position:absolute;left:0;top:0;width:1200px;height:112px;
  background:linear-gradient(var(--bar-top),var(--bar-bottom));
  border-bottom:3px solid var(--rule);
  display:flex;align-items:center;justify-content:center;
}
.masthead h1{
  font-family:"Roboto Condensed",Arial Narrow,sans-serif;font-weight:700;
  font-size:36px;color:var(--white);letter-spacing:.2px;margin-top:-4px;
  text-shadow:0 2px 3px rgba(0,0,0,.7);
}
.amenity-menu{position:absolute;left:0;top:112px;width:242px;height:425px;list-style:none;border-right:1px solid #b9b9b9}
.amenity-menu li{
  height:47.2px;display:flex;align-items:center;padding-left:34px;
  font-weight:700;font-size:20px;color:var(--ink);
  background:linear-gradient(var(--menu-light),var(--menu-dark));
  border-bottom:1px solid #bdbdbd;
  text-shadow:0 1px 1px rgba(255,255,255,.8),0 1px 2px rgba(0,0,0,.25);
}
.amenity-menu li.is-active{
  background:linear-gradient(var(--accent-light),var(--accent-dark));
  color:var(--white);text-shadow:0 1px 2px rgba(0,0,0,.4);
}
.stage{
  position:absolute;left:242px;top:112px;width:958px;height:425px;
  background:linear-gradient(90deg,var(--stage-light),var(--stage-dark));
}
.gallery-frame{
  position:absolute;left:48px;top:43px;width:502px;height:334px;
  background:var(--white);padding:4px;box-shadow:0 1px 4px rgba(0,0,0,.2);
}
.gallery-photo{
  position:relative;width:100%;height:100%;
  background:linear-gradient(180deg,#4c5f8e 0%,#7f8fb4 25%,#8ea0c4 40%,#a4653e 65%,#b8683a 80%,#6e4a35 100%);
}
.zoom-icon{position:absolute;right:10px;bottom:10px}
.gallery-arrow{position:absolute;top:186px}
.gallery-arrow.prev{left:13px}
.gallery-arrow.next{left:560px}
.amenity-copy{position:absolute;left:598px;top:56px;width:340px}
.amenity-copy h2{font-size:31px;font-weight:700;color:var(--ink);margin-bottom:12px}
.amenity-copy p{font-size:14.2px;line-height:23.4px;color:var(--ink-soft)}
.main-nav{
  position:absolute;left:0;top:537px;width:1200px;height:111px;display:flex;
  background:linear-gradient(var(--bar-top),var(--bar-bottom));
  border-top:3px solid var(--rule);
}
.main-nav .nav-item{
  width:140.3px;border-left:1px solid #2b2e31;box-shadow:inset 1px 0 0 #6b7176;
  display:flex;flex-direction:column;align-items:center;justify-content:flex-end;padding-bottom:12px;
  font-family:"Roboto Condensed",Arial Narrow,sans-serif;font-weight:700;font-size:17px;color:var(--white);
  text-shadow:0 2px 2px rgba(0,0,0,.6);
}
.main-nav .nav-item svg{margin-bottom:6px}
.main-nav .nav-home{width:242px;border-left:none;box-shadow:none;justify-content:center;padding:0 0 4px;font-size:30px}
.main-nav .nav-item.is-current{background:linear-gradient(#9a9ea2,#4a4e53)}
.nav-pointer{position:absolute;left:304px;top:528px}
.nav-hint{
  flex:1;border-left:1px solid #2b2e31;box-shadow:inset 1px 0 0 #6b7176;
  display:flex;align-items:center;padding-left:30px;gap:12px;padding-bottom:6px;
  color:var(--white);font-size:18px;line-height:18px;
}
</style>
</head>
<body>
<header class="masthead"><h1>WHERE CONVENIENCE MEETS LUXURY</h1></header>

<ul class="amenity-menu">
  <li>Site map</li>
  <li>Swimming pool</li>
  <li class="is-active">Fitness center</li>
  <li>Tennis court</li>
  <li>Play area</li>
  <li>Gareges</li>
  <li>Club House</li>
  <li>Pets Area</li>
  <li>Proximity to VELTA</li>
</ul>

<main class="stage">
  <svg class="gallery-arrow prev" width="25" height="42" viewBox="0 0 25 42"><defs><linearGradient id="arrowFill" x1="0" y1="0" x2="0" y2="1"><stop offset="0" stop-color="#f5a030"/><stop offset="1" stop-color="#e4601a"/></linearGradient></defs><polygon points="25,0 0,21 25,42" fill="url(#arrowFill)"/></svg>
  <div class="gallery-frame">
    <div class="gallery-photo" role="img" aria-label="Fitness center with a row of treadmills along tall windows, wooden floor and wicker lounge chairs">
      <svg class="zoom-icon" width="34" height="34" viewBox="0 0 34 34" fill="none" stroke="#fff" stroke-width="3" opacity=".85"><circle cx="14" cy="14" r="11"/><line x1="22" y1="22" x2="31" y2="31" stroke-width="5" stroke-linecap="round"/><line x1="14" y1="8" x2="14" y2="20"/><line x1="8" y1="14" x2="20" y2="14"/></svg>
    </div>
  </div>
  <svg class="gallery-arrow next" width="25" height="42" viewBox="0 0 25 42"><polygon points="0,0 25,21 0,42" fill="url(#arrowFill)"/></svg>
  <section class="amenity-copy">
    <h2>Fitness Center</h2>
    <p>Lorem Ipsum is simply dummy text of the printing and typesetting industry. Lorem Ipsum has been the industry's standard dummy text ever since the 1500s, when an unknown printer took a galley of type and scrambled it to make a type specimen book. It has survived not only five centuries, but also the leap into electronic</p>
  </section>
</main>

<svg class="nav-pointer" width="16" height="9" viewBox="0 0 16 9"><polygon points="8,0 16,9 0,9" fill="#3a3e43"/></svg>

<nav class="main-nav">
  <div class="nav-item nav-home">HOME</div>
  <div class="nav-item is-current">
    <svg width="46" height="56" viewBox="0 0 46 56" fill="#fff"><circle cx="23" cy="12" r="6"/><path d="M15 20h16v16h-3v16h-10v-16h-3z"/><circle cx="9" cy="22" r="4.5"/><path d="M3 28h12v12h-2v12h-8v-12h-2z"/><circle cx="37" cy="22" r="4.5"/><path d="M31 28h12v12h-2v12h-8v-12h-2z"/><g stroke="#fff" stroke-width="2"><line x1="23" y1="0" x2="23" y2="3"/><line x1="14" y1="3" x2="16" y2="5"/><line x1="32" y1="3" x2="30" y2="5"/></g></svg>
    COMMUNITY</div>
  <div class="nav-item">
    <svg width="66" height="56" viewBox="0 0 66 56" fill="#fff"><path d="M33 2 4 26h6v26h46V26h6z"/><path d="M25 52V34h16v18z" fill="#4a4f54"/><rect x="30" y="18" width="6" height="6" fill="#4a4f54"/></svg>
    NIGHBORHOOD</div>
  <div class="nav-item">
    <svg width="54" height="54" viewBox="0 0 54 54" fill="#fff"><polygon points="27,2 2,14 52,14"/><rect x="4" y="16" width="46" height="4"/><rect x="8" y="22" width="6" height="20"/><rect x="18" y="22" width="6" height="20"/><rect x="30" y="22" width="6" height="20"/><rect x="40" y="22" width="6" height="20"/><rect x="4" y="44" width="46" height="4"/><rect x="0" y="50" width="54" height="4"/></svg>
    FLOOR PLANS</div>
  <div class="nav-item">
    <svg width="50" height="44" viewBox="0 0 50 44" fill="#fff"><path d="M0 14 25 0l25 14v30H0z"/><path d="M3 16l22 15 22-15" fill="none" stroke="#4a4f54" stroke-width="2.5"/></svg>
    CONTACT US</div>
  <div class="nav-item">
    <svg width="44" height="50" viewBox="0 0 44 50" fill="#fff"><path d="M12 14a10 11 0 0 1 20 0v4a10 11 0 0 1-20 0z"/><path d="M4 50c0-14 6-20 13-22l5 10 5-10c7 2 13 8 13 22z"/></svg>
    COMPANY</div>
  <div class="nav-hint">
    <svg width="26" height="40" viewBox="0 0 26 40" fill="none" stroke="#fff" stroke-width="1.5"><circle cx="10" cy="10" r="9" opacity=".6"/><circle cx="10" cy="10" r="5"/><path d="M7 10v14l-3-2v8c0 4 3 8 8 8h4c4 0 7-3 7-7V20c0-2-3-2-3 0v-1c0-2-3-2-3 0v-1c0-2-3-2-3 0V10c0-2-4-2-4 0z" fill="#fff"/></svg>
    <span>Touch an option<br>to explore</span>
  </div>
</nav>
</body>
</html>
```